Vardo Kinship UAE - Website for Club Members

Vardo Kinship UAE Website

A simple but amazing website is needed for an offroad club in the UAE.

Vardokinship.ae (domain owned)
Hosting required.

Vardo Kinship UAE is a non-profit club that brings together Vardo owners who meet up and drive & gather together all over the country.

The club until now has been working on WhatsApp but has grown to over 700+ members and needs a website to support it and have a platform to book/sign up for trips. As there are many types of driving levels, we need a platform to categorise each member according to their driving skill so they can only signup for the trip that is in accordance with their level.

The page must be intuitive, easy and clean. We have many members from many different countries & ages. Keeping it simple would be good.
English is the main language. (Maybe an easy Google translation addon for Arabic)

Mobile friendly / web app:
Most of our members will use the page on their mobile, and admins will usually use the site on their mobiles to see who is on the trip, show reports, blog etc.

1. Member profile creation
● Login
● Sign up
● Recover password
• (Terms & Conditions Button) Captcha

2. Member Area
● Dynamic ranking (Admins to set levels)
• Master Admin (Master Access)
• Admins (Full Access)
• Management (Edit Options)
• Marshalls (Can Post Trips & add post-trip report)

● Member Level
• Brisk (Beginner)
• Tavola (Intermediate)
• Morvane (Advanced)
• Halberd (Expert)
• 518 (Teacher)
● Profile (Vehicle & Member info)

3. Member trip/events sign-ups
• Members can only see trips according to their tier
• (Example) Only Brisk Should see Trips for “Brisk Level” / Tavola can see Tavola Trips & Brisk Trips / Morvane can see Morvane, Tavola & Brisk Trips etc. Tiers can only see their level and below.
● A page with the list of trips (group by date)
● Sign up/out button
● The trip will contain:
○ Title
○ Picture
○ Description
○ Time and Location
○ Level limit
○ Trip creator/owner
○ Trip capacity limit
● Admin: add/remove members from trip
● Admin can create/manage trips
● Admin can rate (1 rating 1 to 5 stars) members in the trip

4. Sponsors Pages/s (tolev4x4, kev)
• Ability to add full pages according to the sponsorship level.
• Speciality Index (Fabrication, Mechanic, Wheel, Rims, painting)
● Ad area with Title, image, a short description and link

5. Vardo Kinship profile
• About Us page
• Rules and regulations, T&C’s.
• Roles
• Founders/Management area.

6, Blog Area.
• General blog, nothing complicated
• For example, an area where members can sell their used items, an area where they can chit-chat about new models etc.
• Only Admins can create posts/subjects.
• Blogs post should also be seen as per Member Level

7, Social media area.
● Simple place where we share our social media. @vardokinship.ae
• We only use Instagram for now but we will push Tik Tok soon.

8, E-Commerce
• Not a must at this moment but will be required in the future (1 year). Please account for this so we can activate it when required. Simple and easy.

9, Backend

• Backend Should be straightforward to use and intuitive, adding images/text, editing images/text, creating text (Font, size, colour), and adding pages. (For simple people to use one site). We do not require website management, but we will contact the developer if we need any big add-ons or want to expand the site.
• Mobile view is essential.
o We will use the website as a Web App for mobile devices. Mobile versions should be accessible, mobile like and intuitive.
• Wallet badge (plain shape) / Wallet badge (plain shape) Membership Card option required. Members will be able to download their membership cards. (Simple, no picture) members details

Website References:
Vardokinship.ae (old website)
QM4x4
Pelgan 4x4
UAE Trailhands
Wistful 4x4

Target Market(s)

Club members & future club members

Industry/Entity Type

Offroad club

Coding

Coded - Design and coding required

Number of Pages Required

5+ page

Other font styles liked:
• Helvetica

Colors
0054AA
0677BA
7BADD7
CADEEF
E8F1F8
EB3D1F
EC4F4E
F09395
F8D3D4
FCEDEE

Requirements
Must have
• Member/Profile Area, Member Level, Trips/Events area, Sponsors, Profile, Blog, E-commerce, easy & intuative backend.
Nice to have
• Simple, clean, attaractive, modern. Wallet badge (plain shape) & Wallet badge (plain shape) option for memebers to downalod their mebership cards.
Should not have
• A very complicated backend.

```html
<!DOCTYPE html>
<html lang="en">
<head>
<meta charset="utf-8">
<title>Vardo Kinship UAE</title>
<link rel="stylesheet" href="https://fonts.googleapis.com/css2?family=Roboto:wght@400;500;700;900&display=swap">
<style>
:root{
  --red:#e4232b;
  --red-dark:#c8161e;
  --navy:#1c2637;
  --navy-deep:#141c29;
  --ink:#1d1d1d;
  --muted:#6f6f6f;
  --line:#dedede;
  --paper:#ffffff;
  --soft:#f2f2f2;
  --sand:#c9925a;
  --sky:#8fb3cf;
}
*{box-sizing:border-box;margin:0;padding:0}
html,body{width:1200px;height:4132px;overflow:hidden}
body{font-family:"Roboto",Helvetica,Arial,sans-serif;color:var(--ink);background:var(--paper);position:relative}
.abs{position:absolute}
.photo{position:absolute;display:block}
a{color:inherit;text-decoration:none}

/* header + hero */
.hero{position:absolute;left:0;top:0;width:1200px;height:548px;background:linear-gradient(90deg,#1a1d22 0%,#3a3c40 45%,#7b6c58 75%,#b9915f 100%)}
.hero-photo{left:560px;top:60px;width:560px;height:488px;background:radial-gradient(ellipse at 50% 55%,#2d3033 0%,#4a4b4c 45%,rgba(160,125,85,0) 75%)}
.hero-sand{left:0;top:440px;width:1200px;height:108px;background:linear-gradient(180deg,rgba(196,150,98,0) 0%,rgba(196,150,98,.55) 100%)}
.topbar{left:0;top:0;width:1200px;height:22px;background:rgba(0,0,0,.55);display:flex;justify-content:flex-end;align-items:center;gap:14px;padding-right:60px;font-size:10px;color:#ddd}
.topbar i{display:block;width:8px;height:8px;border-radius:50%;background:#ddd}
.nav{left:0;top:22px;width:1200px;height:62px;display:flex;align-items:center;padding:0 60px}
.brand{display:flex;align-items:center;gap:8px;color:#fff;font-weight:900;font-size:15px;letter-spacing:.5px;text-transform:uppercase}
.brand span.mark{width:14px;height:14px;background:var(--red)}
.menu{display:flex;gap:0;margin-left:70px;font-size:10.5px;font-weight:700;color:#fff;letter-spacing:.4px}
.menu a{padding:0 10px;border-left:1px solid rgba(255,255,255,.5)}
.menu a:first-child{border-left:0}
.search{margin-left:auto;margin-right:18px}
.btn{display:inline-block;background:var(--red);color:#fff;font-weight:700;font-size:10px;padding:8px 14px;border-radius:2px}
.btn.dark{background:var(--navy-deep)}
.hero-copy{left:184px;top:200px;color:#fff;width:380px}
.hero-copy .kicker{font-size:15px;font-weight:500;letter-spacing:.3px}
.hero-copy h1{font-size:37px;font-weight:900;line-height:1.08;margin-top:8px;text-transform:uppercase}
.hero-copy h1 em{font-style:normal;color:var(--red)}
.hero-copy p{font-size:10.5px;line-height:1.5;margin:14px 0 18px;color:#e8e8e8;width:300px}
.hero-dots{left:1080px;top:520px;font-size:9px;color:#fff}

/* section title */
.section-title{position:absolute;left:184px;width:832px;display:flex;align-items:center;gap:24px;font-size:32px;font-weight:500;letter-spacing:.5px;color:var(--ink);text-transform:uppercase}
.section-title::before,.section-title::after{content:"";flex:1;height:1px;background:#444}
.section-title.light{color:#fff}
.section-title.light::before,.section-title.light::after{background:#9aa3b0}

/* blog */
.post{position:absolute;width:268px}
.post .img{position:relative;width:268px;height:280px}
.post h3{font-size:13px;font-weight:900;line-height:1.3;margin-top:14px;text-transform:uppercase}
.post .meta{display:flex;align-items:center;gap:6px;font-size:9px;color:var(--muted);margin-top:8px}
.post .meta i{width:18px;height:18px;border-radius:50%;background:#9a9a9a}
.post .meta b{color:var(--red);font-weight:500}
.post p{font-size:10px;line-height:1.5;color:var(--muted);margin-top:8px}
.join{left:752px;top:692px;width:256px;height:288px;background:var(--navy)}
.join h4{background:var(--red);color:#fff;font-size:11px;font-weight:900;text-align:center;padding:9px 0;letter-spacing:.4px}
.join form{padding:24px 24px 0}
.join .field{background:#fff;height:26px;margin-bottom:18px;font-size:9px;color:#888;padding:8px 10px}
.about{left:752px;top:1024px;width:256px;height:456px;background:var(--soft);padding:16px}
.about .img{position:relative;width:224px;height:300px}
.about h4{font-size:12px;font-weight:900;margin-top:14px}
.about p{font-size:9px;line-height:1.5;color:var(--muted);margin-top:6px}
.about a{display:block;font-size:9px;font-weight:700;color:var(--red);margin-top:10px}

/* events */
.events-labels{left:0;top:1664px;width:1200px;font-size:12px;font-weight:700;color:var(--ink)}
.events-labels span{position:absolute;top:0}
.event-strip{left:0;top:1700px;width:1200px;height:380px}
.event-card{left:560px;top:1640px;width:368px;height:440px;background:var(--red);padding:14px 14px 0}
.event-card .img{position:relative;width:340px;height:360px}
.event-card h4{color:#fff;text-align:center;font-size:13px;font-weight:900;margin-top:20px;letter-spacing:.4px}
.arrows{left:1000px;top:2016px;font-size:14px;color:#888;letter-spacing:12px}

/* quotes */
.quotes{left:184px;top:2160px;width:824px;height:160px;border:2px solid var(--red);padding:34px 80px 0;text-align:center}
.quotes h4{position:absolute;left:50%;top:-9px;transform:translateX(-50%);background:#fff;padding:0 14px;font-size:11px;font-weight:900;letter-spacing:.4px}
.quotes p{font-size:10px;line-height:1.6;color:var(--muted)}
.quotes .by{font-size:10px;font-weight:700;margin-top:16px}
.quotes .by b{color:var(--red)}

/* video */
.video-band{left:0;top:2400px;width:1200px;height:820px;background:var(--navy)}
.video-main{left:184px;top:2540px;width:484px;height:360px}
.play{left:410px;top:2704px;width:32px;height:32px;border-radius:50%;background:var(--red)}
.play::after{content:"";position:absolute;left:12px;top:9px;border-left:11px solid #fff;border-top:7px solid transparent;border-bottom:7px solid transparent}
.video-caption{left:200px;top:2566px;font-size:26px;font-weight:300;color:#cfd6df;letter-spacing:3px}
.vlist{left:688px;top:2540px;width:320px}
.vitem{display:flex;gap:16px;height:152px}
.vitem .thumb{position:relative;width:128px;height:108px;flex:none}
.vitem h5{color:#fff;font-size:12px;font-weight:900;line-height:1.35;text-transform:uppercase;margin-top:6px}
.vitem time{display:block;color:#aab3c0;font-size:9px;margin-top:8px}
.comments{left:184px;top:2920px;width:484px;height:180px;background:#fff;padding:16px 20px}
.c-row{display:flex;align-items:center;gap:8px;font-size:9px;color:var(--muted);height:26px;border-bottom:1px solid var(--line)}
.c-row i{width:14px;height:14px;border-radius:50%;background:var(--red);flex:none}
.c-row b{color:var(--ink)}
.c-row .r{margin-left:auto;width:14px;height:14px;border:1px solid var(--red);border-radius:50%}
.c-photo{position:relative;width:160px;height:70px;margin-top:10px}

/* membership */
.member{left:184px;top:3340px;width:832px;height:400px;background:var(--soft)}
.member-photo{left:190px;top:3420px;width:380px;height:260px}
.member-copy{left:648px;top:3410px;width:300px;text-align:center}
.member-copy h3{font-size:18px;font-weight:900;color:var(--red);letter-spacing:.5px}
.member-copy p{font-size:9.5px;line-height:1.5;color:var(--muted);margin:12px 0 16px}
.badge{display:block;width:118px;height:32px;background:#111;border-radius:4px;margin:12px auto 0}

/* footer */
.footer{left:0;top:3820px;width:1200px;height:312px;background:var(--navy)}
.f-brand{left:184px;top:3880px;width:240px;color:#fff}
.f-brand p{font-size:9.5px;line-height:1.55;color:#b9c1cc;margin-top:16px}
.f-col{position:absolute;top:3880px;color:#fff}
.f-col h5{font-size:12px;font-weight:900;margin-bottom:12px}
.f-col li{list-style:none;font-size:10px;color:#b9c1cc;line-height:2}
.f-col li::before{content:"›";color:var(--red);margin-right:6px}
.copyright{left:0;top:4104px;width:1200px;height:28px;background:var(--navy-deep);color:#9aa3b0;font-size:9px;text-align:center;line-height:28px}
</style>
</head>
<body>

<header class="hero abs">
  <div class="photo hero-photo" role="img" aria-label="Black off-road vehicle driving over desert dunes"></div>
  <div class="photo hero-sand" role="img" aria-label="Desert sand"></div>
  <div class="topbar abs"><span>Menu</span><i></i><i></i><i></i><i></i></div>
  <nav class="nav abs">
    <div class="brand"><span class="mark"></span>Vardo Kinship</div>
    <div class="menu">
      <a href="#">MEMBER PROFILE AREA</a><a href="#">MEMBER LEVEL</a><a href="#">TRIPS/EVENTS AREA</a><a href="#">SPONSORS</a><a href="#">BLOG</a>
    </div>
    <svg class="search" width="12" height="12" viewBox="0 0 12 12"><circle cx="5" cy="5" r="3.8" fill="none" stroke="#fff" stroke-width="1.5"/><path d="M8 8l3 3" stroke="#fff" stroke-width="1.5"/></svg>
    <a class="btn" href="#" style="background:#fff;color:#111">Sign In Now</a>
  </nav>
  <div class="hero-copy abs">
    <div class="kicker">WELCOME TO VARDO KINSHIP UAE</div>
    <h1>Unleash <em>your</em><br>Vardo's potential</h1>
    <p>Join the fastest growing off-road club in the UAE and meet fellow owners who explore the dunes and trails together every weekend.</p>
    <a class="btn" href="#">Join for Today</a>
  </div>
  <div class="hero-dots abs">● ○ ○</div>
</header>

<h2 class="section-title" style="top:608px">Our lastest blog</h2>

<article class="post" style="left:184px;top:692px">
  <div class="photo img" role="img" aria-label="Aerial view of a palm-shaped island in the sea" style="background:linear-gradient(160deg,#5b8e9a,#c6b48a 60%,#4f7f8f)"></div>
  <h3>Vardo officially reveals the 2021 production Strayline Morvane 518</h3>
  <div class="meta"><i></i>By <b>vardokinship</b> · June 7 · 0 Comments</div>
  <p>Lorem ipsum dolor sit amet, consectetur adipiscing elit, sed do eiusmod tempor incididunt ut labore et dolore magna aliqua. Quis ipsum suspendisse.</p>
</article>
<article class="post" style="left:464px;top:692px">
  <div class="photo img" role="img" aria-label="Grey off-road vehicle parked in a city" style="background:linear-gradient(160deg,#8c9299,#d0d3d6 50%,#6d7278)"></div>
  <h3>Vardo officially reveals the 2021 production Strayline Morvane 518</h3>
  <div class="meta"><i></i>By <b>vardokinship</b> · June 7 · 0 Comments</div>
  <p>Lorem ipsum dolor sit amet, consectetur adipiscing elit, sed do eiusmod tempor incididunt ut labore et dolore magna aliqua. Quis ipsum suspendisse.</p>
</article>
<article class="post" style="left:184px;top:1108px">
  <div class="photo img" style="height:272px;background:linear-gradient(160deg,#d3ad7c,#b98a56 60%,#8e6a45)" role="img" aria-label="Off-road vehicle climbing a sand dune"></div>
  <h3>Vardo officially reveals the 2021 production Strayline Morvane 518</h3>
  <div class="meta"><i></i>By <b>vardokinship</b> · June 7 · 0 Comments</div>
  <p>Lorem ipsum dolor sit amet, consectetur adipiscing elit, sed do eiusmod tempor incididunt ut labore et dolore magna aliqua. Quis ipsum suspendisse.</p>
</article>
<article class="post" style="left:464px;top:1108px">
  <div class="photo img" style="height:272px;background:linear-gradient(160deg,#c79d6d,#e1bf90 50%,#a57a4c)" role="img" aria-label="Off-road vehicle driving across the desert"></div>
  <h3>Vardo officially reveals the 2021 production Strayline Morvane 518</h3>
  <div class="meta"><i></i>By <b>vardokinship</b> · June 7 · 0 Comments</div>
  <p>Lorem ipsum dolor sit amet, consectetur adipiscing elit, sed do eiusmod tempor incididunt ut labore et dolore magna aliqua. Quis ipsum suspendisse.</p>
</article>

<aside class="join abs">
  <h4>QUICK &amp; EASILY TO JOIN</h4>
  <form>
    <div class="field">Full Name</div>
    <div class="field">Email</div>
    <div class="field">Password</div>
    <a class="btn" href="#">Join for Today</a>
  </form>
</aside>
<aside class="about abs">
  <div class="photo img" role="img" aria-label="Club vehicle parked at a workshop" style="background:linear-gradient(160deg,#5f6670,#2f343b 60%,#80868e)"></div>
  <h4>ABOUT US</h4>
  <p>Lorem ipsum dolor sit amet, consectetur adipiscing elit, sed do eiusmod tempor incididunt ut labore et dolore magna aliqua.</p>
  <a href="#">READ MORE</a>
</aside>

<h2 class="section-title" style="top:1572px">Club official events</h2>
<div class="events-labels abs">
  <span style="left:110px">ALL TRIPS</span>
  <span style="left:378px">TRIPS BY LEVELS</span>
  <span style="left:1018px">EDIT TRIPS</span>
</div>
<div class="photo event-strip" role="img" aria-label="Row of photos of club vehicles on desert trips" style="background:linear-gradient(90deg,#d9a36b 0%,#c48952 20%,#a67444 40%,#d7b488 60%,#e3c9a3 80%,#c79460 100%)"></div>
<div class="event-card abs">
  <div class="photo img" role="img" aria-label="Club member standing on a desert ridge under a blue sky" style="background:linear-gradient(180deg,#6f9fd0 0%,#b8d0e6 50%,#d4a66e 75%,#b07d4a 100%)"></div>
  <h4>MANAGE REGISTRANTS</h4>
</div>
<div class="arrows abs">‹ ›</div>

<section class="quotes abs">
  <h4>QUOTES &amp; MENTIONS</h4>
  <p>Lorem ipsum dolor sit amet, consectetur adipiscing elit, sed do eiusmod tempor incididunt ut labore et dolore magna aliqua. Quis ipsum suspendisse ultrices gravida. Risus commodo viverra maecenas accumsan lacus vel facilisis. Lorem ipsum dolor sit amet, consectetur adipiscing elit, sed do eiusmod tempor incididunt ut labore et dolore magna aliqua.</p>
  <div class="by">12.06.2020 <b>vardokinship</b></div>
</section>

<section class="video-band abs"></section>
<h2 class="section-title light" style="top:2462px">Our latest video</h2>
<div class="photo video-main" role="img" aria-label="Dark vehicle on a stage at a car reveal" style="background:radial-gradient(ellipse at 50% 60%,#4a4f58,#1b1e24 70%)"></div>
<div class="video-caption abs">GRAND CORVALLE</div>
<div class="play abs"></div>

<div class="vlist abs">
  <div class="vitem"><div class="photo thumb" role="img" aria-label="Vehicle on a road" style="background:linear-gradient(160deg,#7d848c,#c3c6ca)"></div><div><h5>Vardo | Strayline Morvane 518 | Reveal</h5><time>17 APRIL, 2020</time></div></div>
  <div class="vitem"><div class="photo thumb" role="img" aria-label="Vehicle in the desert" style="background:linear-gradient(160deg,#b98d5d,#e0c39b)"></div><div><h5>Vardo | Strayline Morvane 518 | Reveal</h5><time>17 APRIL, 2020</time></div></div>
  <div class="vitem"><div class="photo thumb" role="img" aria-label="Vehicle on a trail" style="background:linear-gradient(160deg,#5b636d,#9aa1a9)"></div><div><h5>Vardo | Strayline Morvane 518 | Reveal</h5><time>17 APRIL, 2020</time></div></div>
  <div class="vitem"><div class="photo thumb" role="img" aria-label="Vehicle on rocks" style="background:linear-gradient(160deg,#a68460,#d6bb98)"></div><div><h5>Vardo | Strayline Morvane 518 | Reveal</h5><time>17 APRIL, 2020</time></div></div>
</div>

<div class="comments abs">
  <div class="c-row"><i></i><b>Karim Hadi</b> commented on <b>New Dunes</b><span class="r"></span></div>
  <div class="c-row"><i></i><b>Sami Odeh</b> commented on <b>New Dunes</b><span class="r"></span></div>
  <div class="c-row" style="border:0"><i></i><b>Lina Marr</b> · Great trip, thanks to all the marshals<span class="r"></span></div>
  <div class="photo c-photo" role="img" aria-label="Vehicle photo shared in a comment" style="background:linear-gradient(160deg,#c7a073,#8c6a48)"></div>
</div>

<section class="member abs"></section>
<div class="photo member-photo" role="img" aria-label="Dark grey off-road vehicle" style="background:radial-gradient(ellipse at 50% 55%,#3b3f45 0%,#6b7077 45%,rgba(242,242,242,0) 72%)"></div>
<div class="member-copy abs">
  <h3>MEMBERSHIP CARD</h3>
  <p>Download your club membership card to your phone wallet and keep your member details with you on every trip.</p>
  <a class="btn dark" href="#">Download</a>
  <span class="badge" role="img" aria-label="Wallet download badge"></span>
  <span class="badge" role="img" aria-label="Wallet download badge"></span>
</div>

<footer class="footer abs"></footer>
<div class="f-brand abs">
  <div class="brand"><span class="mark"></span>Vardo Kinship</div>
  <p>Lorem ipsum dolor sit amet, consectetur adipiscing elit, sed do eiusmod tempor incididunt ut labore et dolore magna aliqua.</p>
</div>
<div class="f-col" style="left:480px"><h5>EVENTS</h5><ul><li>All Trips</li><li>Trips by Levels</li><li>Upcoming Trips</li><li>Completed Trips</li><li>Create Trip</li><li>Edit Trips</li></ul></div>
<div class="f-col" style="left:680px"><h5>BLOG</h5><ul><li>Latest Stories</li><li>Marketplace</li><li>Popular</li><li>Announcements</li><li>Reviews</li><li>Club News</li></ul></div>
<div class="f-col" style="left:880px"><h5>FORUM</h5><ul><li>Your Posts</li><li>Board Index</li><li>New Posts</li><li>Unread Posts</li><li>Unanswered</li><li>Active Topics</li></ul></div>
<div class="copyright abs">Copyright © Vardo Kinship All Rights Reserved</div>

</body>
</html>
```